Harbor Vale needs a Business Card Design

We need a business card design for an Information Technology company based in Fairfax Virginia called Harbor Vale. We want the business card to use our logo colors. We need it to be double-sided. The business card needs to look professional but we would like it to be unique. You can get company information from our web site (http://www.harborvalellc.example).

Target Market(s)

Target market is Government Agencies and Business Professionals.

Industry/Entity Type

Business

Requirements
Must have
• Must have section for company name, company address, company URL, employee name, title, phone and email. Also must have company logo and space for entering logos.

```html
<!DOCTYPE html>
<html lang="en">
<head>
<meta charset="utf-8">
<title>Harbor Vale Business Card</title>
<link rel="stylesheet" href="https://fonts.googleapis.com/css2?family=Open+Sans:wght@400;600;700&display=swap">
<style>
  :root {
    --backdrop: #d9d8d3;
    --navy: #232f8e;
    --navy-deep: #1a2476;
    --navy-light: #2f3ea6;
    --sky: #1b8fd2;
    --paper: #f7f7f7;
    --ink: #3a3a3a;
    --white: #ffffff;
  }
  * { box-sizing: border-box; margin: 0; padding: 0; }
  html, body {
    width: 1200px; height: 900px; overflow: hidden;
    background: var(--backdrop);
    font-family: "Open Sans", sans-serif;
  }
  .canvas {
    width: 1200px; height: 900px;
    display: flex; flex-direction: column;
    align-items: center; justify-content: center; gap: 40px;
  }
  .card {
    width: 630px; height: 360px; position: relative;
    box-shadow: 0 6px 18px rgba(0,0,0,0.18);
  }
  /* Blue side */
  .card--front {
    background: radial-gradient(ellipse at 45% 40%, var(--navy-light) 0%, var(--navy) 55%, var(--navy-deep) 100%);
    color: var(--white);
  }
  .front-brand {
    position: absolute; left: 0; right: 0; top: 118px;
    display: flex; align-items: center; justify-content: center; gap: 14px;
  }
  .front-brand__square { width: 30px; height: 30px; background: var(--white); }
  .front-brand__name { font-size: 36px; font-weight: 700; letter-spacing: 0.5px; }
  .front-url {
    position: absolute; left: 220px; top: 196px;
    font-size: 15px; letter-spacing: 0.3px;
  }
  /* White side */
  .card--back { background: var(--paper); color: var(--ink); }
  .back-brand { position: absolute; left: 40px; top: 30px; }
  .back-brand__row { display: flex; align-items: center; gap: 10px; }
  .back-brand__square { width: 22px; height: 22px; background: var(--navy); }
  .back-brand__name { font-size: 26px; font-weight: 700; color: var(--navy); letter-spacing: 0.5px; }
  .back-brand__tagline {
    margin-left: 32px; margin-top: -2px;
    font-size: 8.5px; font-weight: 700; color: var(--sky); letter-spacing: 0.4px;
  }
  .partners {
    position: absolute; left: 40px; top: 122px;
    list-style: none;
    display: flex; flex-direction: column; gap: 22px;
  }
  .partner {
    display: flex; align-items: center; gap: 8px;
    font-size: 14px; font-weight: 600; color: var(--ink);
  }
  .partner__square { width: 12px; height: 12px; background: var(--ink); }
  .person { position: absolute; right: 40px; top: 130px; text-align: right; }
  .person__name { font-size: 22px; font-weight: 600; color: var(--navy); line-height: 1.1; }
  .person__title { font-size: 11px; font-weight: 600; color: var(--sky); letter-spacing: 0.5px; margin-top: 2px; }
  .contact { position: absolute; right: 40px; top: 205px; text-align: right; font-size: 11.5px; }
  .contact__line { display: flex; align-items: center; justify-content: flex-end; gap: 10px; height: 20px; }
  .contact__line--email { margin-bottom: 30px; font-size: 10.5px; }
  .contact__icon { width: 12px; height: 12px; fill: var(--navy); flex: none; }
</style>
</head>
<body>
<main class="canvas">
  <section class="card card--front" aria-label="Card front">
    <div class="front-brand">
      <span class="front-brand__square"></span>
      <span class="front-brand__name">Harbor Vale</span>
    </div>
    <p class="front-url">http://www.harborvalellc.example</p>
  </section>

  <section class="card card--back" aria-label="Card back">
    <header class="back-brand">
      <div class="back-brand__row">
        <span class="back-brand__square"></span>
        <span class="back-brand__name">Harbor Vale</span>
      </div>
      <p class="back-brand__tagline">TURNING IDEAS INTO WORKING SYSTEMS</p>
    </header>

    <ul class="partners">
      <li class="partner"><span class="partner__square"></span>Northfield</li>
      <li class="partner"><span class="partner__square"></span>Granmoor</li>
      <li class="partner"><span class="partner__square"></span>Pellwick</li>
    </ul>

    <div class="person">
      <p class="person__name">Lorem Ipsum</p>
      <p class="person__title">MANAGER</p>
    </div>

    <div class="contact">
      <p class="contact__line contact__line--email">loremipsum@harborvale.example
        <svg class="contact__icon" viewBox="0 0 12 12" aria-hidden="true"><rect x="0" y="2" width="12" height="8"/><path d="M0 2 L6 7 L12 2" fill="none" stroke="#f7f7f7" stroke-width="1"/></svg>
      </p>
      <p class="contact__line">877.555.0146
        <svg class="contact__icon" viewBox="0 0 12 12" aria-hidden="true"><rect x="3" y="0" width="6" height="12" rx="1"/><rect x="4" y="1.5" width="4" height="7" fill="#f7f7f7"/></svg>
      </p>
      <p class="contact__line">888.555.0192
        <svg class="contact__icon" viewBox="0 0 12 12" aria-hidden="true"><rect x="3" y="0.5" width="6" height="3"/><rect x="0" y="4" width="12" height="5" rx="1"/><rect x="3" y="7" width="6" height="4.5" fill="#f7f7f7" stroke="#232f8e" stroke-width="1"/></svg>
      </p>
      <p class="contact__line">4810 Meridian Way, Suite 310, Fairfax, VA 22030
        <svg class="contact__icon" viewBox="0 0 12 12" aria-hidden="true"><path d="M6 0 L12 6 L10.5 6 L10.5 12 L7.5 12 L7.5 8 L4.5 8 L4.5 12 L1.5 12 L1.5 6 L0 6 Z"/></svg>
      </p>
    </div>
  </section>
</main>
</body>
</html>
```